Business Card design for Brightvale Global

we need a business card design for our company. we are a trading company based in LA.

Company Name: Brightvale Global Corp.
Contact: Marcus Ortega
Title: CEO
Tel: 310-647-2093
Email: bvgcorp7@mailnest.example

Target Market(s)

International, especially China

Industry/Entity Type

Trade

Colors
3276b5
34a7d8
0555a3
0493ce
85cae6
85acd3
d0dfed
cee9f5

Requirements
Must have
• Logo and contact, to have international/global feeling

```html
<!DOCTYPE html>
<html lang="en">
<head>
<meta charset="utf-8">
<title>Brightvale Global – Business Card</title>
<link href="https://fonts.googleapis.com/css2?family=Lato:wght@400;700&family=Montserrat:wght@600&display=swap" rel="stylesheet">
<style>
  :root {
    --stage: #1f1f1f;
    --paper: #ffffff;
    --brand-blue: #2688cf;
    --brand-navy: #16365f;
    --ink-grey: #3a3a3a;
    --back-deep: #173c6e;
    --back-mid: #2a8bd0;
    --back-light: #3a9ade;
  }
  * { box-sizing: border-box; margin: 0; padding: 0; }
  html, body {
    width: 1200px; height: 900px; overflow: hidden;
    background: var(--stage);
    font-family: "Lato", Arial, sans-serif;
  }
  .stage { position: relative; width: 1200px; height: 900px; }
  .card {
    position: absolute; top: 306px;
    width: 440px; height: 271px;
    border-radius: 10px; overflow: hidden;
    box-shadow: 3px 4px 6px rgba(0,0,0,0.55);
  }
  .card-front { left: 149px; background: var(--paper); }
  .card-back {
    left: 608px;
    background: linear-gradient(125deg, var(--back-deep) 0%, var(--back-mid) 45%, var(--back-light) 55%, var(--back-deep) 100%);
  }
  .wordmark {
    position: absolute; display: flex; align-items: center; gap: 10px;
    font-family: "Lato", Arial, sans-serif; font-weight: 700;
    font-size: 27px; letter-spacing: -0.3px; white-space: nowrap;
  }
  .wordmark-dot { width: 22px; height: 22px; border-radius: 50%; flex: none; }
  .card-front .wordmark { right: 22px; top: 380px; top: 78px; color: var(--brand-navy); }
  .card-front .wordmark-dot { background: var(--brand-blue); }
  .card-back .wordmark {
    left: 50%; top: 50%; transform: translate(-50%, -50%); color: #ffffff;
  }
  .card-back .wordmark-dot { background: #ffffff; }
  .holder { position: absolute; left: 24px; top: 152px; }
  .holder-name {
    font-family: "Montserrat", Arial, sans-serif; font-weight: 600;
    font-size: 14.5px; color: var(--brand-navy); letter-spacing: 0.2px;
  }
  .holder-name .first { color: var(--brand-blue); }
  .holder-title { font-size: 12.5px; color: var(--ink-grey); margin-top: 1px; }
  .contact-list { position: absolute; left: 24px; top: 207px; list-style: none; }
  .contact-item {
    display: flex; align-items: center; gap: 3px;
    font-size: 12.5px; color: var(--ink-grey); line-height: 16px;
  }
  .contact-icon { width: 13px; height: 13px; flex: none; }
  .band { position: absolute; left: 0; bottom: 0; height: 16px; width: 100%; display: flex; }
  .band-light { width: 218px; background: var(--brand-blue); }
  .band-dark { flex: 1; background: var(--brand-navy); }
</style>
</head>
<body>
<main class="stage">
  <section class="card card-front" aria-label="Business card front">
    <div class="wordmark"><span class="wordmark-dot"></span>Brightvale Global</div>
    <div class="holder">
      <p class="holder-name"><span class="first">MARCUS</span> ORTEGA</p>
      <p class="holder-title">CEO</p>
    </div>
    <ul class="contact-list">
      <li class="contact-item">
        <svg class="contact-icon" viewBox="0 0 14 14"><circle cx="7" cy="7" r="7" fill="var(--brand-blue)"/><path d="M3.6 6.2c0-1.2 1.5-2 3.4-2s3.4.8 3.4 2l-1.3.4-.4-1H5.3l-.4 1zM4.6 7h4.8l.6 3H4z" fill="#fff"/></svg>
        310-647-2093
      </li>
      <li class="contact-item">
        <svg class="contact-icon" viewBox="0 0 14 14"><circle cx="7" cy="7" r="7" fill="var(--brand-blue)"/><rect x="3.5" y="4.5" width="7" height="5" fill="#fff"/><path d="M3.5 4.5L7 7.4l3.5-2.9" fill="none" stroke="var(--brand-blue)" stroke-width="0.8"/></svg>
        bvgcorp7@mailnest.example
      </li>
    </ul>
    <div class="band"><span class="band-light"></span><span class="band-dark"></span></div>
  </section>
  <section class="card card-back" aria-label="Business card back">
    <div class="wordmark"><span class="wordmark-dot"></span>Brightvale Global</div>
  </section>
</main>
</body>
</html>
```